Etiketten-Design für neue Biermarke
Zielgruppe
Es soll eine neue Biermarke entwickelt werden. Die drei grundlegenden Sorten sind: Pils, Radler, Helles. Für die neue Biermarke soll ein Markenname, ein Logo und ein Etikettendesign gestaltet werden. Das Bier soll traditionell sein und den typischen Biertrinker ansprechen. Die Zielgruppe der Biermarke ist die breite Masse. Das Bier soll für 9,90€ verkauft werden.
Aufgabenstellung
Das Design der Etiketten sollte klassisch und traditionell wirken. Es dürfen gerne klassische, historische und urige Elemente wie Hopfen, Bierfass, altertümliche Illustrationen, etc. verwendet werden. Das Bier sollte weder in Richtung eines Craft Bieres noch in die Richtung eines jungen/hippen Bieres gehen.

```html
<!DOCTYPE html>
<html lang="de">
<head>
<meta charset="utf-8">
<title>Falkenbrunn Pilsner – Helles Etikett</title>
<link href="https://fonts.googleapis.com/css2?family=Playfair+Display+SC:wght@700&family=Lobster&display=swap" rel="stylesheet">
<style>
  :root {
    --brown: #2b0f08;
    --cream: #f2d28c;
    --cream-light: #f7e3ab;
    --red: #a3001b;
    --red-dark: #6c0011;
    --white: #ffffff;
    --page: #ffffff;
  }
  html, body {
    margin: 0;
    padding: 0;
    width: 812px;
    height: 1200px;
    overflow: hidden;
    background: var(--page);
  }
  .label {
    display: block;
    width: 812px;
    height: 1200px;
  }
  .label-body { fill: var(--cream); stroke: var(--brown); stroke-width: 6; }
  .stripe-field { fill: url(#stripes); }
  .stripe-base { fill: var(--cream); }
  .stripe-line { fill: var(--cream-light); }
  .brand-arc, .quality-arc {
    font-family: "Playfair Display SC", "Playfair Display", serif;
    font-weight: 700;
    fill: var(--brown);
  }
  .brand-arc { font-size: 74px; }
  .quality-arc { font-size: 54px; }
  .artwork { fill: var(--brown); }
  .ribbon-band { fill: var(--red); }
  .ribbon-tail { fill: var(--red); }
  .ribbon-fold { fill: var(--red-dark); }
  .variety {
    font-family: "Lobster", cursive;
    font-size: 112px;
    fill: var(--white);
  }
  .year {
    font-family: "Playfair Display SC", "Playfair Display", serif;
    font-weight: 700;
    font-size: 64px;
    fill: var(--brown);
    letter-spacing: 3px;
  }
</style>
</head>
<body>
<svg class="label" viewBox="0 0 812 1200" xmlns="http://www.w3.org/2000/svg">
  <defs>
    <pattern id="stripes" width="29" height="40" patternUnits="userSpaceOnUse" x="150">
      <rect class="stripe-base" width="29" height="40"/>
      <rect class="stripe-line" x="0" width="10" height="40"/>
    </pattern>
    <clipPath id="label-shape">
      <rect x="29" y="29" width="754" height="1142" rx="377"/>
    </clipPath>
    <path id="brand-path" d="M 120.4,356.6 A 290,290 0 0 1 691.6,356.6"/>
    <path id="quality-path" d="M 115.5,942 A 326,326 0 0 0 696.5,942"/>
  </defs>

  <rect class="label-body" x="29" y="29" width="754" height="1142" rx="377"/>
  <rect class="stripe-field" x="144" y="172" width="524" height="863" rx="262"/>

  <text class="brand-arc">
    <textPath href="#brand-path" startOffset="50%" text-anchor="middle" textLength="790" lengthAdjust="spacingAndGlyphs">FALKENBRUNN PILSNER</textPath>
  </text>

  <g class="artwork" role="img" aria-label="Weizenähre links">
    <rect x="58" y="378" width="70" height="262" rx="35"/>
  </g>
  <g class="artwork" role="img" aria-label="Weizenähre rechts">
    <rect x="684" y="378" width="70" height="262" rx="35"/>
  </g>

  <g class="artwork" role="img" aria-label="Illustration: zwei Männer in Tracht halten ein Wappen mit Turmkrone, darunter gekreuzte Ähren und Hopfendolden">
    <rect x="205" y="285" width="400" height="345" rx="40"/>
  </g>

  <g clip-path="url(#label-shape)">
    <path class="ribbon-tail" d="M 20,705 L 110,700 L 110,810 L 20,860 Z"/>
    <path class="ribbon-tail" d="M 792,705 L 702,700 L 702,810 L 792,860 Z"/>
    <path class="ribbon-fold" d="M 100,800 L 150,805 L 140,840 Z"/>
    <path class="ribbon-fold" d="M 712,800 L 662,805 L 672,840 Z"/>
    <path class="ribbon-band" d="M 93,665 Q 406,630 719,665 L 700,808 Q 406,775 112,808 Z"/>
  </g>

  <text class="variety" x="406" y="760" text-anchor="middle">Helles</text>

  <text class="year" x="406" y="903" text-anchor="middle">· 1897 ·</text>

  <text class="quality-arc">
    <textPath href="#quality-path" startOffset="50%" text-anchor="middle" textLength="690" lengthAdjust="spacingAndGlyphs">DEUTSCHE BRAUQUALITÄT</textPath>
  </text>
</svg>
</body>
</html>
```